Newly created Management Consulting company needs a brochure to capture clients's interest

This is a new management consulting firm providing service in Finance, Marketing, Operations/Manufacturing Strategy, and Project Management.
Please go to the company's website: www.talvenbridgeadvisory.ca . The website is pretty straightforward and gives a clear explanation of all the services and sub-services offered. Based on the existent material on the website, I would like to create a company's brochure that can inspire clients to seek our services.
One important thing: the slogan/tagline ("Shaping the future of your business") needs to be added somewhere in the vicinity of our company's' LOGO. Please see attached the company's logo (JPEG file).
The brochure size and number of pages can vary, depending on the layout of the brochure so it can fit the content, so I am open to different and innovative sizes/shapes and no. of pages etc. Graphics should combine real pictures with graphic design technology, and should give a professional look and feel comparable to big companies' marketing materials.
Updates
The brochure does not necessarily have to include pictures that are on the website. If you think that other pictures and graphics can deliver a stronger message to customers, by all means I am open to any other ideas.
Thanks.
As I said before, the pictures do not need to be exactly the same pictures as on the website, if you can bring in other cool pictures to attract clients, please go ahead. Also, you do not need to use only black background, if you have better colors ideas to combine with the our LOGO, and it looks good, by all means do use other colors. But our LOGO needs to be represented as it is on the JPEG I attached.
May the most creative and cool design win! Good luck!
Please ensure that all the content of our website fits into your brochure, including our contact information. It is up to you to come up with the necessary number of pages, design and shape of the brochure, but the text should be clear enough to be read by a normal person without a magnifying glass.
Thank you.
In order to keep the brochure to a reasonable number of pages, I agree that it is not necessary to include 100% all the text that appears on the website. That being said, even if you do not have enough space to include all the background and introduction paragraphs under each service/sub-service, it is still important that the main message for each service/sub-service is being contained in the brochure.
Target Market(s)
Our clients are companies with sizes starting from 10-20 employees and up to large Corvane 300 companies.
Industry/Entity Type
Management Consulting
Look and feel

```html
<!DOCTYPE html>
<html lang="en">
<head>
<meta charset="utf-8">
<title>Talvenbridge Advisory – Brochure</title>
<link rel="stylesheet" href="https://fonts.googleapis.com/css2?family=Oswald:wght@400;600;700&family=Questrial&display=swap">
<style>
  :root {
    --stage: #66766a;
    --green: #3c9f35;
    --green-deep: #23801f;
    --green-light: #8dc63f;
    --green-pale: #e4f2d2;
    --green-mist: #c5e3a1;
    --black: #121212;
    --white: #ffffff;
    --yellow: #f4e61c;
    --orange: #f26a22;
    --red: #e2231a;
    --blue: #29a8e0;
    --grey: #c9cbc8;
    --ink: #2b3a2b;
    --photo-office: #8fa6b8;
  }
  * { box-sizing: border-box; margin: 0; padding: 0; }
  html, body { width: 1200px; height: 848px; overflow: hidden; }
  body {
    background: var(--stage);
    font-family: 'Questrial', sans-serif;
    position: relative;
  }

  .spread { position: absolute; display: flex; box-shadow: 0 6px 18px rgba(0,0,0,.3); }
  .spread--outside { left: 70px; top: 50px; }
  .spread--inside { left: 70px; top: 360px; }
  .front-cover-large { position: absolute; left: 700px; top: 112px; box-shadow: 0 10px 28px rgba(0,0,0,.35); }
  svg { display: block; }

  .brand-name { font-family: 'Oswald', sans-serif; font-weight: 400; fill: var(--white); letter-spacing: 1px; }
  .service { font-family: 'Oswald', sans-serif; font-weight: 400; fill: var(--yellow); font-size: 15px; }
  .tagline { font-family: 'Oswald', sans-serif; font-weight: 700; }
  .tagline--yellow { fill: var(--yellow); }
  .tagline--white { fill: var(--white); }
  .contact { font-family: 'Questrial', sans-serif; fill: var(--ink); font-size: 10px; }
  .contact--label { fill: var(--black); }

  .inner-page {
    position: relative;
    width: 230px; height: 324px;
    background: linear-gradient(160deg, var(--green-pale), #f4faec 55%, var(--green-mist));
    overflow: hidden;
  }
  .inner-page + .inner-page { border-left: 1px solid rgba(0,0,0,.12); }
  .section-band {
    position: absolute;
    background: var(--green-deep);
    color: var(--white);
    font-family: 'Oswald', sans-serif;
    font-weight: 600;
    font-size: 9px;
    line-height: 1.1;
    padding: 4px 6px;
  }
  .body-copy {
    position: absolute;
    font-size: 5.6px;
    line-height: 1.45;
    color: var(--ink);
    text-align: left;
  }
  .highlight-word {
    position: absolute;
    font-family: 'Oswald', sans-serif;
    font-weight: 600;
    color: var(--green-deep);
    font-size: 9px;
    line-height: 1;
  }
  .photo {
    position: absolute;
    background: linear-gradient(135deg, #d7dee4, var(--photo-office) 60%, #5d6f7f);
  }
  .chart { position: absolute; }
  .chart-label { font-size: 4.5px; color: var(--ink); text-align: center; }
</style>
</head>
<body>

  <div class="spread spread--outside">
    <svg class="back-cover" width="190" height="268" viewBox="0 0 440 620">
      <defs>
        <linearGradient id="back-bg" x1="0" y1="0" x2="1" y2="1">
          <stop offset="0" stop-color="#eef7df"/>
          <stop offset="1" stop-color="#b7dc8b"/>
        </linearGradient>
      </defs>
      <rect width="440" height="620" fill="url(#back-bg)"/>
      <rect y="395" width="440" height="62" fill="var(--black)"/>
      <rect x="211" y="404" width="18" height="18" fill="var(--green-light)"/>
      <text class="brand-name" x="220" y="440" font-size="17" text-anchor="middle">TALVENBRIDGE ADVISORY</text>
      <text class="contact contact--label" x="220" y="478" text-anchor="middle">Office Address:</text>
      <text class="contact" x="220" y="492" text-anchor="middle">Suite 400, 18 Harlow Street, Kingsford</text>
      <text class="contact" x="220" y="506" text-anchor="middle">Ontario, Canada K7L 2P4</text>
      <text class="contact" x="220" y="520" text-anchor="middle">Phone: 613-555-0148</text>
      <text class="contact" x="220" y="534" text-anchor="middle">Email: info@talvenbridgeadvisory.ca</text>
      <text class="contact" x="220" y="552" text-anchor="middle" fill="var(--green-deep)">www.talvenbridgeadvisory.ca</text>
      <rect x="200" y="564" width="40" height="40" fill="var(--grey)" role="img" aria-label="Social network links"/>
    </svg>
    <svg class="front-cover-small" width="190" height="268" viewBox="0 0 440 620">
      <use href="#front-cover" width="440" height="620"/>
    </svg>
  </div>

  <div class="spread spread--inside">
    <div class="inner-page inner-page--left">
      <div class="section-band" style="left:0; top:22px; width:120px;">Helping<br>you reach the summit</div>
      <p class="body-copy" style="left:8px; top:56px; width:214px;">Someone who has seen the ups and downs of business from many perspectives can help you chart a clear path. We listen, study your market and build with you a practical plan to reach your goals with confidence.</p>
      <span class="highlight-word" style="left:60px; top:96px;">vision</span>
      <span class="highlight-word" style="left:88px; top:108px;">motivation</span>
      <div class="photo" style="left:0; top:124px; width:108px; height:112px;" role="img" aria-label="Consultants meeting around a conference table"></div>
      <div class="section-band" style="left:110px; top:140px; width:76px;">Rethinking Operations and Manufacturing</div>
      <p class="body-copy" style="left:112px; top:186px; width:62px;">We review your processes, supply chain and plant layout to remove waste, lift quality and cut cost, so every improvement shows up on your bottom line.</p>
      <span class="highlight-word" style="left:180px; top:184px; font-size:8px;">Improve<br>BottomLine</span>
      <div class="chart" style="left:180px; top:206px; width:44px;">
        <div class="chart-label">Cost Structure</div>
        <svg width="44" height="32" viewBox="0 0 44 32">
          <circle cx="22" cy="16" r="7.5" fill="none" stroke="var(--blue)" stroke-width="15" stroke-dasharray="15 47.1" transform="rotate(-90 22 16)"/>
          <circle cx="22" cy="16" r="7.5" fill="none" stroke="var(--red)" stroke-width="15" stroke-dasharray="0 15 14 33.1" transform="rotate(-90 22 16)"/>
          <circle cx="22" cy="16" r="7.5" fill="none" stroke="var(--green)" stroke-width="15" stroke-dasharray="0 29 18 15.1" transform="rotate(-90 22 16)"/>
          <circle cx="22" cy="16" r="7.5" fill="none" stroke="#7b4fa0" stroke-width="15" stroke-dasharray="0 47 15.1 0" transform="rotate(-90 22 16)"/>
        </svg>
      </div>
      <div class="section-band" style="left:0; top:244px; width:104px;">Maximize<br>Shareholders Value</div>
      <p class="body-copy" style="left:8px; top:274px; width:160px;">Sound finance functions turn data into decisions. We help you plan capital, manage risk and report clearly so your company grows its value year after year.</p>
      <div class="chart" style="left:180px; top:262px; width:44px;">
        <div class="chart-label">Revenue Mix</div>
        <svg width="44" height="32" viewBox="0 0 44 32">
          <circle cx="22" cy="16" r="7.5" fill="none" stroke="#7b4fa0" stroke-width="15" stroke-dasharray="20 27.1" transform="rotate(-90 22 16)"/>
          <circle cx="22" cy="16" r="7.5" fill="none" stroke="var(--blue)" stroke-width="15" stroke-dasharray="0 20 16 26.1" transform="rotate(-90 22 16)"/>
          <circle cx="22" cy="16" r="7.5" fill="none" stroke="var(--yellow)" stroke-width="15" stroke-dasharray="0 36 14 12.1" transform="rotate(-90 22 16)"/>
          <circle cx="22" cy="16" r="7.5" fill="none" stroke="var(--green)" stroke-width="15" stroke-dasharray="0 50 12.1 0" transform="rotate(-90 22 16)"/>
        </svg>
      </div>
    </div>

    <div class="inner-page inner-page--right">
      <div class="section-band" style="left:0; top:14px; width:108px;">Unleash the Power of<br>Marketing and Sales</div>
      <div class="photo" style="right:0; top:8px; width:112px; height:118px;" role="img" aria-label="Business team reviewing results at a computer"></div>
      <p class="body-copy" style="left:8px; top:50px; width:102px;">From spotting trends to building campaigns, we shape marketing and sales plans that reach the right buyers and turn interest into lasting revenue.</p>
      <div class="section-band" style="left:0; top:124px; width:112px;">Turn Project Management into a Strategic Advantage</div>
      <p class="body-copy" style="left:8px; top:168px; width:110px;">Proven methods and hands-on coaching give your managers the tools to run projects well, so every initiative is delivered on time and on budget.</p>
      <span class="highlight-word" style="left:130px; top:168px;">Inspire</span>
      <span class="highlight-word" style="left:140px; top:180px;">Team</span>
      <span class="highlight-word" style="left:150px; top:192px;">Achievement</span>
      <div class="photo" style="left:14px; top:212px; width:204px; height:104px;" role="img" aria-label="Consultant presenting a plan at a whiteboard to colleagues"></div>
    </div>
  </div>

  <svg class="front-cover-large" width="440" height="620" viewBox="0 0 440 620">
    <defs>
      <linearGradient id="cover-green" x1="0" y1="0" x2="1" y2="1">
        <stop offset="0" stop-color="#a5d65a"/>
        <stop offset=".55" stop-color="#4fae39"/>
        <stop offset="1" stop-color="#237f1f"/>
      </linearGradient>
      <linearGradient id="photo-office" x1="0" y1="0" x2="1" y2="1">
        <stop offset="0" stop-color="#e3e8ec"/>
        <stop offset=".55" stop-color="#8fa6b8"/>
        <stop offset="1" stop-color="#4c5b68"/>
      </linearGradient>
      <linearGradient id="photo-money" x1="0" y1="0" x2="1" y2="1">
        <stop offset="0" stop-color="#e7cfc5"/>
        <stop offset="1" stop-color="#a87f86"/>
      </linearGradient>
      <symbol id="front-cover" viewBox="0 0 440 620">
        <rect width="440" height="620" fill="url(#cover-green)"/>
        <path d="M0 450 C170 450 360 360 440 220 L440 620 L0 620 Z" fill="var(--black)"/>

        <rect x="300" y="0" width="118" height="100" fill="var(--black)"/>
        <rect x="352" y="22" width="14" height="14" fill="var(--green-light)"/>
        <text class="brand-name" x="359" y="64" font-size="14" text-anchor="middle">TALVENBRIDGE</text>
        <text class="brand-name" x="359" y="80" font-size="9" text-anchor="middle" letter-spacing="3">ADVISORY</text>

        <polygon points="190,70 300,180 190,290 80,180" fill="url(#photo-office)" role="img" aria-label="Team of consultants reviewing documents in a bright office"/>

        <g role="img" aria-label="Banknotes of several currencies">
          <rect x="118" y="300" width="62" height="62" fill="url(#photo-money)" transform="rotate(-25 149 331)"/>
          <rect x="228" y="272" width="58" height="58" fill="url(#photo-money)" transform="rotate(-25 257 301)"/>
          <rect x="200" y="350" width="60" height="60" fill="url(#photo-money)" transform="rotate(-25 230 380)"/>
        </g>

        <rect x="58" y="318" width="24" height="24" fill="var(--yellow)" transform="rotate(-20 70 330)"/>
        <rect x="108" y="418" width="38" height="38" fill="var(--blue)" transform="rotate(-20 127 437)"/>

        <g transform="translate(270 248) rotate(-15)">
          <text class="service" x="0" y="0">Finance</text>
          <text class="service" x="10" y="20">Marketing</text>
          <rect x="0" y="28" width="13" height="13" fill="var(--orange)" transform="rotate(45 6.5 34.5)"/>
          <text class="service" x="16" y="40">Operations</text>
          <rect x="22" y="48" width="13" height="13" fill="var(--red)" transform="rotate(45 28.5 54.5)"/>
          <text class="service" x="30" y="60">Project Management</text>
        </g>

        <g transform="translate(208 540) rotate(-15)">
          <rect x="-46" y="-30" width="42" height="42" fill="var(--grey)"/>
          <text class="tagline tagline--white" x="-14" y="10" font-size="22" transform="rotate(-90 -14 10)">the</text>
          <text class="tagline tagline--yellow" x="30" y="-48" font-size="32">Shaping</text>
          <text class="tagline tagline--yellow" x="-2" y="6" font-size="46">future</text>
          <text class="tagline tagline--white" x="124" y="-16" font-size="18" font-weight="400">of</text>
          <text class="tagline tagline--white" x="142" y="6" font-size="22" font-weight="400">your</text>
          <text class="tagline tagline--white" x="-6" y="62" font-size="60">business</text>
        </g>
      </symbol>
    </defs>
    <use href="#front-cover" width="440" height="620"/>
  </svg>

</body>
</html>
```